business card for an electronic retail store

take our existing color logo, design a new business card and make a black&white version of the logo as well

Industry/Entity Type

Electronic

```html
<!DOCTYPE html>
<html lang="en">
<head>
<meta charset="utf-8">
<title>Kestrel Business Card</title>
<link rel="stylesheet" href="https://fonts.googleapis.com/css2?family=Exo+2:wght@400;500&display=swap">
<style>
  :root {
    --backdrop: #2b2b2d;
    --card: #0c0c0c;
    --accent: #f7d117;
    --text: #f2f2f2;
    --muted: #9a9a9a;
    --icon-ink: #0c0c0c;
  }
  html, body {
    margin: 0;
    width: 1200px;
    height: 816px;
    overflow: hidden;
    background: var(--backdrop);
  }
  .canvas {
    position: relative;
    width: 1200px;
    height: 816px;
  }
  .card {
    position: absolute;
    left: 75px;
    top: 108px;
    width: 1050px;
    height: 600px;
    border-radius: 40px;
    background: var(--card);
    font-family: "Exo 2", sans-serif;
    color: var(--text);
    overflow: hidden;
  }
  .person {
    position: absolute;
    left: 70px;
    top: 138px;
    display: flex;
    align-items: center;
    gap: 18px;
  }
  .person .avatar {
    width: 48px;
    height: 48px;
  }
  .person .name {
    margin: 0;
    font-size: 25px;
    font-weight: 500;
    letter-spacing: 2px;
    text-transform: uppercase;
    line-height: 1.1;
  }
  .person .role {
    margin: 2px 0 0;
    font-size: 21px;
    font-weight: 400;
    letter-spacing: 1.5px;
    line-height: 1.1;
  }
  .divider {
    position: absolute;
    left: 70px;
    top: 232px;
    width: 500px;
    height: 5px;
    background: var(--accent);
  }
  .contacts {
    position: absolute;
    left: 78px;
    top: 300px;
    margin: 0;
    padding: 0;
    list-style: none;
  }
  .contacts li {
    display: flex;
    align-items: center;
    gap: 22px;
    height: 66px;
    margin-bottom: 16px;
  }
  .contacts .icon {
    flex: none;
    width: 52px;
    height: 52px;
    border-radius: 50%;
    background: var(--accent);
    display: flex;
    align-items: center;
    justify-content: center;
  }
  .contacts .icon svg {
    width: 28px;
    height: 28px;
  }
  .contacts .lines {
    font-size: 20px;
    letter-spacing: 1.5px;
    line-height: 1.3;
  }
  .brand {
    position: absolute;
    left: 620px;
    top: 232px;
    width: 380px;
  }
  .brand .name {
    margin: 0;
    font-size: 64px;
    font-weight: 500;
    color: var(--accent);
    letter-spacing: 1px;
    line-height: 1;
  }
  .brand .tagline {
    margin: 14px 0 0 4px;
    font-size: 23px;
    font-weight: 400;
    color: var(--text);
    letter-spacing: 1px;
  }
</style>
</head>
<body>
<div class="canvas">
  <section class="card">
    <div class="person">
      <svg class="avatar" viewBox="0 0 48 48" aria-hidden="true">
        <circle cx="24" cy="24" r="24" fill="var(--muted)"/>
        <circle cx="24" cy="18" r="7" fill="var(--card)"/>
        <path d="M11 36c2-7 7-10 13-10s11 3 13 10z" fill="var(--card)"/>
      </svg>
      <div>
        <p class="name">Marcus Reed</p>
        <p class="role">Managing Director</p>
      </div>
    </div>

    <div class="divider"></div>

    <ul class="contacts">
      <li>
        <span class="icon">
          <svg viewBox="0 0 24 24" aria-hidden="true">
            <rect x="7" y="2" width="10" height="20" rx="2" fill="none" stroke="var(--icon-ink)" stroke-width="2"/>
            <circle cx="12" cy="18" r="1.2" fill="var(--icon-ink)"/>
          </svg>
        </span>
        <span class="lines">012 345 6789<br>012 345 6789</span>
      </li>
      <li>
        <span class="icon">
          <svg viewBox="0 0 24 24" aria-hidden="true">
            <rect x="2" y="4" width="20" height="13" rx="1.5" fill="none" stroke="var(--icon-ink)" stroke-width="2"/>
            <path d="M9 21h6M12 17v4" stroke="var(--icon-ink)" stroke-width="2"/>
          </svg>
        </span>
        <span class="lines">urname@email.com<br>urwebsitename.com</span>
      </li>
      <li>
        <span class="icon">
          <svg viewBox="0 0 24 24" aria-hidden="true">
            <path d="M12 2a7 7 0 0 0-7 7c0 5 7 13 7 13s7-8 7-13a7 7 0 0 0-7-7z" fill="var(--icon-ink)"/>
            <circle cx="12" cy="9" r="2.6" fill="var(--accent)"/>
          </svg>
        </span>
        <span class="lines">047,12th floor,Harbor Crest<br>Road LKG</span>
      </li>
    </ul>

    <div class="brand">
      <p class="name">Kestrel</p>
      <p class="tagline">Home Electronics Store</p>
    </div>
  </section>
</div>
</body>
</html>
```